Banner Ad Design Project

We are a quality Digital Printer and we are erecting a roadside banner to promote "walk In" - "drive In" customers

The attached document gives the position and copy for the DUFFIELD banner, please ignore the AIREDALE banner

The copy on the banner is by no means fixed, I am looking for creative thinking and call to attention reactionary graphics

please delete reference to "Litho" - it is not required

good luck and thank you

regards

Gareth

```html
<!DOCTYPE html>
<html lang="en">
<head>
<meta charset="utf-8">
<title>Ashcombe roadside banner</title>
<link href="https://fonts.googleapis.com/css2?family=Oswald:wght@300;400;700&family=Varela+Round&display=swap" rel="stylesheet">
<style>
  :root {
    --page: #ffffff;
    --post: #cfd1d2;
    --ground: #9a9a9a;
    --header-bg: #bcdcf0;
    --brand-blue: #1d5ea8;
    --center-dark: #23272f;
    --headline: #e9e9e9;
    --ribbon: #5cb3dc;
    --ribbon-shadow: #3a4656;
    --base-strip: #86a8cf;
    --strip-white: #ffffff;
    --phone: #cf2459;
  }
  html, body {
    margin: 0;
    padding: 0;
    overflow: hidden;
    background: var(--page);
  }
  .canvas {
    position: relative;
    width: 775px;
    height: 1200px;
    overflow: hidden;
    background: var(--page);
  }
  .post {
    position: absolute;
    top: 36px;
    width: 35px;
    height: 1137px;
    background: var(--post);
  }
  .post--left { left: 127px; }
  .post--right { left: 601px; }
  .ground {
    position: absolute;
    left: 20px;
    top: 1173px;
    width: 742px;
    height: 1px;
    background: var(--ground);
  }
  .header-board {
    position: absolute;
    left: 162px;
    top: 67px;
    width: 439px;
    height: 147px;
    background: var(--header-bg);
    display: flex;
    align-items: center;
    justify-content: center;
    gap: 16px;
  }
  .brand-mark {
    width: 34px;
    height: 34px;
    background: var(--brand-blue);
  }
  .brand-name {
    font-family: "Varela Round", sans-serif;
    font-size: 54px;
    color: var(--brand-blue);
    letter-spacing: 1px;
  }
  .poster {
    position: absolute;
    left: 162px;
    top: 227px;
    width: 439px;
    height: 585px;
    overflow: hidden;
    background: var(--base-strip);
  }
  .poster__art {
    position: absolute;
    left: 0;
    top: 0;
    width: 439px;
    height: 585px;
  }
  .poster__headline {
    position: absolute;
    left: 0;
    top: 120px;
    width: 439px;
    margin: 0;
    text-align: center;
    font-family: "Varela Round", sans-serif;
    font-weight: 400;
    font-size: 64px;
    line-height: 70px;
    color: var(--headline);
  }
  .poster__cta {
    position: absolute;
    left: 22px;
    top: 374px;
    margin: 0;
    font-family: "Oswald", sans-serif;
    font-weight: 300;
    font-size: 56px;
    letter-spacing: -3px;
    color: #ffffff;
    text-shadow: 0 0 2px #2a2f38, 1px 1px 0 #2a2f38;
  }
  .poster__phone {
    position: absolute;
    left: 166px;
    top: 452px;
    margin: 0;
    font-family: "Oswald", sans-serif;
    font-weight: 700;
    font-size: 46px;
    letter-spacing: 0;
    color: var(--phone);
    transform: rotate(-4deg);
    transform-origin: left center;
  }
</style>
</head>
<body>
<div class="canvas">
  <div class="post post--left"></div>
  <div class="post post--right"></div>
  <div class="ground"></div>

  <header class="header-board">
    <span class="brand-mark"></span>
    <span class="brand-name">ASHCOMBE</span>
  </header>

  <section class="poster">
    <svg class="poster__art" viewBox="0 0 439 585" xmlns="http://www.w3.org/2000/svg">
      <defs>
        <radialGradient id="bloom" cx="0.5" cy="0.3" r="0.75">
          <stop offset="0" stop-color="#23272f"/>
          <stop offset="0.3" stop-color="#23272f"/>
          <stop offset="0.42" stop-color="#2a78c8"/>
          <stop offset="0.55" stop-color="#c12fc9"/>
          <stop offset="0.7" stop-color="#e7c93a"/>
          <stop offset="0.85" stop-color="#3fcf8a"/>
          <stop offset="1" stop-color="#e23a6a"/>
        </radialGradient>
      </defs>
      <rect class="poster__flower" x="0" y="0" width="439" height="520" fill="url(#bloom)" role="img" aria-label="Close-up photograph of a flower with multicoloured petals around a dark centre"/>
      <polygon class="poster__white-strip" points="0,491 146,481 126,545 0,548" fill="var(--strip-white)"/>
      <polygon class="poster__ribbon-shadow" points="94,522 400,500 392,538 94,575" fill="var(--ribbon-shadow)"/>
      <polygon class="poster__ribbon" points="148,454 439,431 439,514 161,547" fill="var(--ribbon)"/>
    </svg>
    <h1 class="poster__headline">digital<br>print</h1>
    <p class="poster__cta">CALL IN NOW</p>
    <p class="poster__phone">01 134550199</p>
  </section>
</div>
</body>
</html>
```